RW Soundworks Web Site Design

Need a basic site to show clients a little about what we do. We are a custom audio video company in the high-end residential market. Need a few basic but professional pages to show past projects and products we sell. No e-commerce. Should include my new logo from MarkHive.

Industry/Entity Type

Residential

Number of Pages Required

2 page

Font styles to use
Serif
Sans Serif

Colors
f78f20

Requirements
Must have
• Company Logo, Send feedback page
Nice to have
• I have no ideas about design, but I do know what I like and dislike when I see it.

```html
<!DOCTYPE html>
<html lang="en">
<head>
<meta charset="utf-8">
<title>RW Soundworks</title>
<link href="https://fonts.googleapis.com/css2?family=Open+Sans:ital,wght@0,400;0,600;0,700;1,400&family=Oswald:wght@500;700&display=swap" rel="stylesheet">
<style>
:root{
  --orange:#f78f20;
  --ink:#1b1b1b;
  --text:#555;
  --muted:#999;
  --soft:#f4f4f4;
  --line:#e3e3e3;
  --dark:#1d1d1d;
  --btn:#c9c9c9;
}
*{box-sizing:border-box;margin:0;padding:0}
html,body{width:1200px;height:2829px;overflow:hidden}
body{font-family:"Open Sans",Arial,sans-serif;color:var(--text);background:#fff;position:relative}
.abs{position:absolute}

/* header */
.brand{left:73px;top:19px;display:flex;align-items:center;gap:12px}
.brand-mark{width:54px;height:54px;background:var(--orange)}
.brand-name{font-weight:700;font-size:26px;color:var(--ink);letter-spacing:.5px;line-height:1}
.social{left:766px;top:36px;display:flex;gap:8px}
.social span{width:22px;height:22px;border-radius:50%;background:#b3b3b3}
.social span:first-child{background:var(--orange)}
.search{left:931px;top:33px;width:193px;height:31px;border:1px solid var(--line);border-radius:16px;font-size:12px;color:var(--muted);padding:7px 14px}
.search svg{position:absolute;right:12px;top:8px}
.nav{left:73px;top:99px;width:1051px;height:38px;background:#111;border-radius:19px;display:flex;align-items:center;justify-content:space-around;padding:0 20px}
.nav a{color:#fff;text-decoration:none;font-size:14px;font-weight:600;text-transform:uppercase;position:relative}
.nav a+a::before{content:"";position:absolute;left:-20px;top:3px;width:1px;height:14px;background:var(--orange)}

/* hero */
.hero{left:0;top:156px;width:1200px;height:518px;background:linear-gradient(180deg,#cfc8bf 0%,#bdb2a5 45%,#a99b8a 75%,#d8d2ca 100%)}
.hero-banner{left:306px;top:156px;width:573px;height:130px;background:var(--orange);text-align:center;padding-top:14px;font-family:Oswald,"Arial Narrow",sans-serif;color:#fff;text-transform:uppercase;white-space:nowrap}
.hero-banner::after{content:"";position:absolute;left:50%;bottom:-18px;margin-left:-18px;border:18px solid transparent;border-bottom:0;border-top-color:var(--orange)}
.hero-banner .l1{font-size:30px;font-weight:500;line-height:52px}
.hero-banner .l1 b{font-size:48px;font-weight:700;color:var(--ink);vertical-align:-3px}
.hero-banner .l2{font-size:27px;font-weight:500;line-height:38px;letter-spacing:-.2px}
.hero-arrow{top:388px;width:48px;height:48px;border-radius:50%;background:#fff;display:flex;align-items:center;justify-content:center}

/* section titles */
.title{border-left:3px solid var(--orange);padding-left:10px;text-transform:uppercase;color:var(--ink)}
.title small{display:block;font-size:15px;font-weight:400;line-height:18px}
.title strong{display:block;font-size:22px;font-weight:700;line-height:26px}

/* welcome */
.welcome{left:0;top:674px;width:1200px;height:375px;background:var(--soft)}
.welcome-text{left:73px;top:782px;width:504px;font-size:13px;line-height:20px}
.welcome-text p+p{margin-top:20px}
.btn-orange{left:73px;top:973px;width:96px;height:29px;background:var(--orange);color:#fff;font-size:11px;font-weight:600;text-align:center;line-height:29px;text-transform:uppercase}
.video{left:613px;top:719px;width:514px;height:283px;background:radial-gradient(circle at 50% 35%,#6f6a66 0%,#3a2c22 35%,#160f0b 100%)}
.play{left:840px;top:836px;width:58px;height:58px;border-radius:50%;border:3px solid #fff;display:flex;align-items:center;justify-content:center}

/* cards */
.card{width:270px;text-align:center}
.diamond{width:167px;height:167px;margin:34px auto 0;border-radius:18px;transform:rotate(45deg);border:4px solid #eee}
.card h3{margin-top:56px;font-size:14px;font-weight:600;color:var(--ink);text-transform:uppercase}
.card p{margin-top:10px;font-size:13px;line-height:19px;padding:0 12px}
.card .btn{display:inline-block;margin-top:12px;width:94px;height:27px;line-height:27px;background:var(--btn);color:#fff;font-size:11px;font-weight:600;text-transform:uppercase}

/* testimonials */
.testimonials{left:0;top:1617px;width:1200px;height:339px;background:var(--soft)}
.quote{top:1754px;width:335px;height:160px;background:#fff;box-shadow:0 1px 3px rgba(0,0,0,.08)}
.quote .avatar{position:absolute;left:20px;top:-26px;width:61px;height:61px;background:linear-gradient(#8a8a8a,#d6d0c9)}
.quote .who{position:absolute;left:104px;top:10px;font-size:14px;font-weight:600;color:var(--ink);text-transform:uppercase}
.quote p{position:absolute;left:20px;top:48px;right:18px;font-size:12.5px;font-style:italic;line-height:19px}

/* footer */
.footer{left:0;top:2527px;width:1200px;height:302px;background:var(--dark);color:#8a8a8a}
.foot-brand{left:73px;top:2600px;display:flex;align-items:center;gap:10px;white-space:nowrap}
.foot-brand .mark{width:52px;height:52px;background:#444}
.foot-brand .name{font-size:17px;font-weight:700;color:#777}
.foot-copy{left:73px;top:2718px;width:240px;font-size:11px;line-height:18px}
.foot-col{top:2570px;width:240px}
.foot-col h4{color:#fff;font-size:14px;font-weight:700;text-transform:uppercase;margin-bottom:18px}
.post{font-size:11.5px;line-height:17px;padding-bottom:16px;margin-bottom:16px;border-bottom:1px solid #333}
.post .date{font-size:9.5px;color:#666;margin-bottom:4px}
.post .body{color:#aaa}
.contact{display:flex;gap:14px;align-items:flex-start;font-size:11.5px;line-height:17px;color:#aaa;margin-bottom:22px}
.contact .ico{flex:none;width:32px;height:32px;border-radius:50%;background:#3a3a3a;display:flex;align-items:center;justify-content:center}
</style>
</head>
<body>

<header>
  <div class="abs brand"><span class="brand-mark"></span><span class="brand-name">RW SOUNDWORKS</span></div>
  <div class="abs social"><span></span><span></span><span></span><span></span><span></span></div>
  <div class="abs search">Enter Your Keyword
    <svg width="14" height="14" viewBox="0 0 14 14"><circle cx="6" cy="6" r="4.5" fill="none" stroke="#999" stroke-width="1.6"/><line x1="9.5" y1="9.5" x2="13" y2="13" stroke="#999" stroke-width="1.6"/></svg>
  </div>
  <nav class="abs nav">
    <a>Home</a><a>About</a><a>Projects</a><a>Services</a><a>Products</a><a>Blog</a><a>Gallery</a><a>Resources</a><a>Testimonials</a><a>Contact</a>
  </nav>
</header>

<section>
  <div class="abs hero" role="img" aria-label="Bright living room with wall-mounted television, wooden media wall and two armchairs"></div>
  <div class="abs hero-banner">
    <div class="l1">We are a custom <b>Audio Video</b></div>
    <div class="l2">Company in the high-end residential market</div>
  </div>
  <div class="abs hero-arrow" style="left:70px"><svg width="14" height="14" viewBox="0 0 14 14"><path d="M9 2 4 7l5 5" fill="none" stroke="#333" stroke-width="2"/></svg></div>
  <div class="abs hero-arrow" style="left:1077px"><svg width="14" height="14" viewBox="0 0 14 14"><path d="M5 2l5 5-5 5" fill="none" stroke="#333" stroke-width="2"/></svg></div>
</section>

<section>
  <div class="abs welcome"></div>
  <div class="abs title" style="left:73px;top:719px"><small>Welcome to</small><strong>RW Soundworks</strong></div>
  <div class="abs welcome-text">
    <p>In publishing and graphic design, lorem ipsum is a filler text commonly used to demonstrate the graphic elements of a document or visual presentation. Replacing meaningful content with placeholder text allows viewers to focus on graphic aspects such as font, typography, and page layout without being distracted by the content.</p>
    <p>It also reduces the need for the designer to come up with meaningful text, as they can instead use quickly-generated lorem ipsum.</p>
  </div>
  <div class="abs btn-orange">Read More</div>
  <div class="abs video" role="img" aria-label="Dark home theater room with projection screen and seating"></div>
  <div class="abs play"><svg width="20" height="22" viewBox="0 0 20 22"><path d="M3 2l15 9-15 9z" fill="#fff"/></svg></div>
</section>

<section>
  <div class="abs title" style="left:73px;top:1091px"><small>Past</small><strong>Projects</strong></div>
  <div class="abs card" style="left:58px;top:1168px"><div class="diamond" role="img" aria-label="Media room with projector screen" style="background:linear-gradient(135deg,#e6dfd3,#8a5a32)"></div><h3>Project Name Here 1</h3><p>It also reduces the need for the designer to come up with meaningful quickly-generated lorem ipsum.</p><span class="btn">Read More</span></div>
  <div class="abs card" style="left:327px;top:1168px"><div class="diamond" role="img" aria-label="Home theater with sofa and wall lighting" style="background:linear-gradient(135deg,#d7a36a,#2d1a10)"></div><h3>Project Name Here 1</h3><p>It also reduces the need for the designer to come up with meaningful quickly-generated lorem ipsum.</p><span class="btn">Read More</span></div>
  <div class="abs card" style="left:598px;top:1168px"><div class="diamond" role="img" aria-label="Wall-mounted television above cabinet" style="background:linear-gradient(135deg,#f0ece6,#5b524a)"></div><h3>Project Name Here 1</h3><p>It also reduces the need for the designer to come up with meaningful quickly-generated lorem ipsum.</p><span class="btn">Read More</span></div>
  <div class="abs card" style="left:867px;top:1168px"><div class="diamond" role="img" aria-label="Theater room with curtains and screen" style="background:linear-gradient(135deg,#c4733a,#3a1708)"></div><h3>Project Name Here 1</h3><p>It also reduces the need for the designer to come up with meaningful quickly-generated lorem ipsum.</p><span class="btn">Read More</span></div>
</section>

<section>
  <div class="abs testimonials"></div>
  <div class="abs title" style="left:73px;top:1662px"><small>Client's</small><strong>Testimonials</strong></div>
  <div class="abs quote" style="left:73px"><div class="avatar" role="img" aria-label="Client portrait"></div><div class="who">John Smith</div><p>"It was popularized in the 1960s with the lorem release of Letraset sheets containing Lorem is a Ipsum passages, and more recently with Maker including versions of Lorem Ipsum."</p></div>
  <div class="abs quote" style="left:434px"><div class="avatar" role="img" aria-label="Client portrait"></div><div class="who">John Smith</div><p>"It was popularized in the 1960s with the lorem release of Letraset sheets containing Lorem is a Ipsum passages, and more recently with Maker including versions of Lorem Ipsum."</p></div>
  <div class="abs quote" style="left:797px;width:330px"><div class="avatar" role="img" aria-label="Client portrait"></div><div class="who">John Smith</div><p>"It was popularized in the 1960s with the lorem release of Letraset sheets containing Lorem is a Ipsum passages, and more recently with Maker including versions of Lorem Ipsum."</p></div>
</section>

<section>
  <div class="abs title" style="left:73px;top:2006px"><small>Our</small><strong>Products</strong></div>
  <div class="abs card" style="left:58px;top:2080px"><div class="diamond" role="img" aria-label="Close-up of a camera lens" style="background:radial-gradient(circle,#6a5a4a,#111)"></div><h3>Project Name Here 1</h3><p>It also reduces the need for the designer to come up with meaningful quickly-generated lorem ipsum.</p><span class="btn">Read More</span></div>
  <div class="abs card" style="left:327px;top:2080px"><div class="diamond" role="img" aria-label="Stereo amplifier and receiver stack" style="background:linear-gradient(135deg,#f4f4f4,#9c9c9c)"></div><h3>Project Name Here 1</h3><p>It also reduces the need for the designer to come up with meaningful quickly-generated lorem ipsum.</p><span class="btn">Read More</span></div>
  <div class="abs card" style="left:598px;top:2080px"><div class="diamond" role="img" aria-label="Tablet with blue screen" style="background:linear-gradient(135deg,#3a2a20,#1aa0e0)"></div><h3>Project Name Here 1</h3><p>It also reduces the need for the designer to come up with meaningful quickly-generated lorem ipsum.</p><span class="btn">Read More</span></div>
  <div class="abs card" style="left:867px;top:2080px"><div class="diamond" role="img" aria-label="Handheld remote control" style="background:linear-gradient(135deg,#6f5aa8,#1a1a2a)"></div><h3>Project Name Here 1</h3><p>It also reduces the need for the designer to come up with meaningful quickly-generated lorem ipsum.</p><span class="btn">Read More</span></div>
</section>

<footer>
  <div class="abs footer"></div>
  <div class="abs foot-brand"><span class="mark"></span><span class="name">RW SOUNDWORKS</span></div>
  <div class="abs foot-copy">© 2015 RW Soundworks, All Rights Reserved<br>Terms and Conditions | Privacy Policy | Terms of Use</div>

  <div class="abs foot-col" style="left:342px">
    <h4>Recent Blog</h4>
    <div class="post"><div class="date">10 MAR 2015 | 10 Comments</div><div class="body">Mirum est notare quam littera gothi ca, quam nunc</div></div>
    <div class="post" style="border:0"><div class="date">10 MAR 2015 | 10 Comments</div><div class="body">Mirum est notare quam littera gothi ca, quam nunc</div></div>
  </div>
  <div class="abs foot-col" style="left:613px">
    <h4>Recent News</h4>
    <div class="post"><div class="date">10 MAR 2015</div><div class="body">Mirum est notare quam littera gothi ca, quam nunc</div></div>
    <div class="post" style="border:0"><div class="date">10 MAR 2015</div><div class="body">Mirum est notare quam littera gothi ca, quam nunc</div></div>
  </div>
  <div class="abs foot-col" style="left:884px">
    <h4>Get in Touch</h4>
    <div class="contact"><span class="ico"><svg width="12" height="16" viewBox="0 0 12 16"><path d="M6 0a6 6 0 0 0-6 6c0 4.5 6 10 6 10s6-5.5 6-10a6 6 0 0 0-6-6zm0 8.5A2.5 2.5 0 1 1 6 3.5a2.5 2.5 0 0 1 0 5z" fill="#ddd"/></svg></span><span>228, Lorem ipsum dolor amet<br>sit amet sor- 859584</span></div>
    <div class="contact"><span class="ico"><svg width="14" height="14" viewBox="0 0 14 14"><path d="M3 0l2.5 3.5-1.5 1.8a8 8 0 0 0 4.7 4.7L10.5 8.5 14 11l-1.5 2.5C6 14 0 8 .5 1.5z" fill="#ddd"/></svg></span><span>Phone :<br>(000) 88 888 8888</span></div>
    <div class="contact"><span class="ico"><svg width="14" height="11" viewBox="0 0 14 11"><rect x=".5" y=".5" width="13" height="10" fill="none" stroke="#ddd"/><path d="M.5.5 7 6l6.5-5.5" fill="none" stroke="#ddd"/></svg></span><span>Email :<br>info@rwsoundworks.com</span></div>
  </div>
</footer>

</body>
</html>
```